Flyer Design

I need a flyer as Iam starting a business which cleans Leather couches,sofas,chairs for residential and businesses.
We clean the interiors of automobiles and marine craft, boats large and small.
We would like to be able to get across the message that we are affordable, personal and reliable.
The Gold coast is our market and within this area there is a large amount of holiday apartments and houses which do experience high traffic to their living and dinning areas.

Target Market(s)

Target market Home,Apartment,Marine and Auto Owners

Industry/Entity Type

Residential

Requirements
Must have
• The flyer must have Company name which is BRIGHT HIDE CARE MOBILE NUMBER
0471932054
EMAIL marvtolk@quellnet.com
Colours would like bright Gold or green or Red eith black lettering very modern font
Nice to have
• I would like to keep it as simple and clean looking.but eye catching
Should not have
• Dont want the flyer to look like a Real Estate flyer or a pizza advertisement.

```html
<!DOCTYPE html>
<html lang="en">
<head>
<meta charset="utf-8">
<title>Bright Hide Care – Leather Cleaning Flyer</title>
<link rel="stylesheet" href="https://fonts.googleapis.com/css2?family=Smythe&family=Oswald:wght@400;500&family=Saira+Condensed:wght@400;500&display=swap">
<style>
  :root {
    --gold: #6b5533;
    --ink: #231f20;
    --sofa-light: #dcd9d7;
    --paper: #ffffff;
    --white: #ffffff;
  }
  * { margin: 0; padding: 0; box-sizing: border-box; }
  html, body { width: 932px; height: 1200px; overflow: hidden; background: var(--paper); }
  .flyer {
    position: relative;
    width: 932px;
    height: 1200px;
    background: var(--paper);
    overflow: hidden;
  }
  .brand-name {
    position: absolute;
    top: 42px;
    left: 0;
    width: 100%;
    text-align: center;
    font-family: "Smythe", serif;
    font-weight: 400;
    font-size: 196px;
    line-height: 196px;
    color: var(--gold);
    letter-spacing: 1px;
  }
  .brand-name span { display: block; }
  .service-line {
    position: absolute;
    top: 474px;
    left: 0;
    width: 100%;
    text-align: center;
    font-family: "Oswald", sans-serif;
    font-weight: 400;
    font-size: 43px;
    line-height: 80px;
    color: var(--ink);
  }
  .service-line span { display: block; }
  .sofa-artwork {
    position: absolute;
    top: 655px;
    left: 45px;
    width: 840px;
    height: 256px;
    display: block;
  }
  .contact-band {
    position: absolute;
    top: 910px;
    left: 0;
    width: 100%;
    height: 290px;
    background: var(--ink);
    text-align: center;
    font-family: "Saira Condensed", sans-serif;
    color: var(--white);
  }
  .contact-heading {
    position: absolute;
    top: 46px;
    left: 0;
    width: 100%;
    font-family: "Oswald", sans-serif;
    font-size: 21px;
    font-weight: 400;
  }
  .contact-row {
    position: absolute;
    left: 0;
    width: 100%;
    white-space: nowrap;
  }
  .contact-row .label {
    color: var(--gold);
    text-transform: uppercase;
    font-weight: 500;
  }
  .contact-row.phone { top: 84px; }
  .contact-row.phone .label { font-size: 36px; margin-right: 8px; }
  .contact-row.phone .value { font-size: 68px; font-weight: 500; letter-spacing: 1px; }
  .contact-row.email { top: 184px; }
  .contact-row.email .label { font-size: 34px; margin-right: 4px; }
  .contact-row.email .value { font-size: 37px; }
</style>
</head>
<body>
  <main class="flyer">
    <h1 class="brand-name"><span>bright hide</span><span>care</span></h1>

    <p class="service-line">
      <span>We clean leather couches, sofas,chairs</span>
      <span>for residential and businesses.</span>
    </p>

    <svg class="sofa-artwork" viewBox="0 0 840 256" role="img" aria-label="Black and white illustration of a leather sofa with two seat cushions">
      <defs>
        <linearGradient id="sofaTone" x1="0" y1="0" x2="0" y2="1">
          <stop offset="0" stop-color="#dcd9d7"/>
          <stop offset="0.55" stop-color="#8a8586"/>
          <stop offset="1" stop-color="#231f20"/>
        </linearGradient>
      </defs>
      <rect x="0" y="0" width="840" height="256" rx="24" fill="url(#sofaTone)"/>
      <rect x="0" y="200" width="840" height="56" fill="#231f20"/>
    </svg>

    <section class="contact-band">
      <p class="contact-heading">Contact us:</p>
      <p class="contact-row phone"><span class="label">Mobile number</span> <span class="value">0471932054</span></p>
      <p class="contact-row email"><span class="label">Email</span> <span class="value">marvtolk@quellnet.com</span></p>
    </section>
  </main>
</body>
</html>
```